Vireo M.K. - Diagnostic Ultrasound Flyer

About US
Vireo M.K. is a concierge ultrasound company that provides onsite or offsite diagnostic ultrasounds. We have over 14 years experience in sonography, business management, and customer service. We offer both the physician and patient flexibility, convenience, and access to timely services.

We provide ultrasounds for the following specialties:
Obstetrics/Gynecology
Abdominal
Small Parts
Vascular

Company Features:
1. Onsite or Offsite Scans
2. Images Available Immediately for Referring Physician and Patient
3. Flexible Options for Ultrasound Interpretation/Billing
4. Access to Interpreting Radiologist
5. Final Report Process - 1-2 Business Days/ 1 hour for STAT.
6. PACS Storage with Secure Access.

We need a place to add in our contact information (address, email, website, phone)

We already have a logo and would like to use it ( they are attached). We would the colors to match the logo colors....maybe lighter version of yellow and blue.

```html
<!DOCTYPE html>
<html lang="en">
<head>
<meta charset="utf-8">
<title>Vireo M.K. – Diagnostic Ultrasound Flyer</title>
<link rel="stylesheet" href="https://fonts.googleapis.com/css2?family=Barlow:ital,wght@0,400;0,500;0,600;0,700;1,500&display=swap">
<style>
  :root {
    --backdrop: #e3e3e6;
    --paper: #ffffff;
    --slate: #5b6383;
    --navy: #27348f;
    --sun: #f2b705;
    --green: #b2c66f;
    --green-light: #d3e0a6;
    --green-accent: #9fb651;
    --photo-warm: #d8d2c8;
    --photo-cool: #8f949a;
  }
  * { box-sizing: border-box; margin: 0; padding: 0; }
  html, body {
    width: 1200px; height: 835px; overflow: hidden;
    background: var(--backdrop);
    font-family: "Barlow", Arial, sans-serif;
  }
  .flyer {
    position: absolute; left: 326px; top: 30px;
    width: 548px; height: 775px;
    background: var(--paper); overflow: hidden;
    box-shadow: 0 6px 24px rgba(0,0,0,.12);
  }
  .hero-photo {
    position: absolute; left: 0; top: 0; width: 548px; height: 360px;
    background: linear-gradient(120deg, var(--photo-warm) 0%, #e9e5df 40%, var(--photo-cool) 75%, #c9ccd0 100%);
  }
  .color-fields { position: absolute; left: 0; top: 0; }
  .brand {
    position: absolute; left: 0; top: 0; width: 210px; height: 72px;
    background: var(--paper); border-bottom-right-radius: 10px;
    display: flex; align-items: center; gap: 8px; padding-left: 22px;
  }
  .brand-dot { width: 12px; height: 12px; border-radius: 50%; background: var(--sun); }
  .brand-name { font-weight: 700; font-size: 26px; color: var(--navy); letter-spacing: .5px; }
  .features-card {
    position: absolute; left: 0; top: 281px; width: 245px; height: 431px;
    background: var(--paper); border-radius: 0 10px 10px 0;
    box-shadow: 2px 3px 8px rgba(0,0,0,.1);
    padding: 26px 20px 0 32px;
  }
  .features-title {
    font-weight: 700; font-size: 20px; letter-spacing: 3px; line-height: 23px;
    color: var(--slate); margin-bottom: 20px;
  }
  .features-title span { display: block; color: var(--green-accent); }
  .features-list { list-style: none; }
  .features-list li {
    position: relative; padding-left: 17px; margin-bottom: 14px;
    font-size: 13.5px; font-weight: 500; line-height: 18px; color: var(--slate);
  }
  .features-list li::before {
    content: ""; position: absolute; left: 2px; top: 6px;
    width: 6px; height: 6px; border-radius: 50%; background: var(--green-accent);
  }
  .about {
    position: absolute; left: 279px; top: 362px; width: 250px; color: var(--paper);
  }
  .about-title { font-weight: 700; font-size: 18px; margin-bottom: 4px; }
  .about-text { font-size: 11.3px; line-height: 14.5px; }
  .about-text em { font-weight: 500; }
  .specialties { position: absolute; left: 279px; top: 530px; width: 250px; }
  .specialties-title {
    font-weight: 700; font-size: 14px; line-height: 19px; color: var(--slate);
    text-transform: uppercase; margin-bottom: 14px;
  }
  .specialty-grid {
    display: grid; grid-template-columns: 104px 104px; gap: 10px 11px;
  }
  .specialty {
    height: 60px; border-radius: 8px; background: var(--paper);
    display: flex; align-items: center; justify-content: center; text-align: center;
    font-size: 13px; font-weight: 600; line-height: 15px; color: var(--slate);
  }
  .contact-bar {
    position: absolute; left: 0; bottom: 0; width: 548px; height: 40px;
    background: var(--paper);
    display: flex; align-items: center; justify-content: center;
    font-size: 11px; color: var(--slate); text-transform: uppercase; letter-spacing: .2px;
  }
  .contact-bar strong { font-weight: 700; margin: 0 3px; }
</style>
</head>
<body>
<main class="flyer">
  <div class="hero-photo" role="img" aria-label="Photo of an ultrasound machine with a monitor and control panel beside a potted plant in a clinic room"></div>

  <svg class="color-fields" width="548" height="775" viewBox="0 0 548 775" aria-hidden="true">
    <rect x="0" y="420" width="548" height="315" fill="var(--green-light)"/>
    <path d="M240 320 C330 322 430 310 548 262 L548 505 C470 530 390 492 240 518 Z" fill="var(--green)"/>
  </svg>

  <header class="brand">
    <span class="brand-dot"></span>
    <span class="brand-name">Vireo M.K.</span>
  </header>

  <section class="features-card">
    <h2 class="features-title">COMPANY<span>FEATURES</span></h2>
    <ul class="features-list">
      <li>Onsite or Offsite Scans</li>
      <li>Images Available Immediately for Referring Physician and Patient</li>
      <li>Flexible Options for Ultrasound Interpretation/Billing</li>
      <li>Access to Interpreting Radiologist</li>
      <li>Final Report Process - 1-2 Business Days/ 1 hour for STAT</li>
      <li>PACS Storage with Secure Access</li>
    </ul>
  </section>

  <section class="about">
    <h2 class="about-title">ABOUT US</h2>
    <p class="about-text"><em>Vireo M.K.</em> is a concierge ultrasound company that provides onsite or offsite diagnostic ultrasounds. We have over 14 years experience in sonography, business management, and customer service. We offer both the physician and patient flexibility, convenience, and access to timely services.</p>
  </section>

  <section class="specialties">
    <h2 class="specialties-title">We provide ultrasounds<br>for the following specialties</h2>
    <div class="specialty-grid">
      <div class="specialty">Obstetrics/<br>Gynecology</div>
      <div class="specialty">Abdominal</div>
      <div class="specialty">Small Parts</div>
      <div class="specialty">Vascular</div>
    </div>
  </section>

  <footer class="contact-bar">
    Contact us to make an appointment: <strong>www.vireo-mk.com</strong> or <strong>email info@vireo-mk.com</strong>
  </footer>
</main>
</body>
</html>
```